Label Design Project for my tea product Imported from Japan

I have a tea importing business. I want someone to help me design a label for my Uji matcha tea product. I want the label to be modern, neat, and beautifully designed. I prefer it to be easily adaptable to other tea products that I will be importing.
Product name: Organic Hoshiba Matcha
Company name: Calm Harbor Leaf Merchants
Description: Powdered Green Tea Matcha
Ceremonial grade premium quality
Directly imported from Japan
This product is going to be sold in the U.S. market, so please make sure that the label is in compliance with the BQC regulations.

Target Market(s)

High end tea consumers

Industry/Entity Type

Business

Requirements
Must have
• Marking of origin : product of Japan
• Imported by: Calm Harbor Leaf Merchants
• Leave space for Net weight, the name and place of business of the manufacturer.
• Ingredients: Green Tea 100%
• Nutrition list is not necessary.

```html
<!DOCTYPE html>
<html lang="en">
<head>
<meta charset="utf-8">
<title>Organic Hoshiba Matcha – Label</title>
<link rel="stylesheet" href="https://fonts.googleapis.com/css2?family=Amatic+SC:wght@400;700&family=Arimo:wght@400;700&display=swap">
<style>
  :root {
    --page: #ffffff;
    --leaf-light: #79c94a;
    --leaf-stripe: #8fd45f;
    --moon: #b9e59a;
    --leaf-dark: #2f6a17;
    --leaf-deep: #275a12;
    --ink-dark: #1f3d0c;
    --text-light: #ffffff;
    --badge-bg: #ffffff;
    --badge-ink: #4a9a2a;
  }
  * { margin: 0; padding: 0; box-sizing: border-box; }
  html, body {
    width: 720px; height: 1200px; overflow: hidden;
    background: var(--page);
  }
  .canvas { position: relative; width: 720px; height: 1200px; }
  .label {
    position: absolute; left: 38px; top: 37px;
    width: 644px; height: 1091px; overflow: hidden;
    background-color: var(--leaf-light);
    background-image: repeating-linear-gradient(90deg,
      transparent 0 22px, var(--leaf-stripe) 22px 24px, transparent 24px 31px);
  }
  .moon {
    position: absolute; left: 55px; top: 90px;
    width: 580px; height: 580px; border-radius: 50%;
    background: var(--moon); opacity: 0.85;
  }
  .hills { position: absolute; inset: 0; width: 644px; height: 1091px; }
  .product-kicker, .product-name {
    position: absolute; left: 0; width: 100%; text-align: center;
    font-family: "Amatic SC", cursive; color: var(--text-light);
    text-transform: uppercase; letter-spacing: 5px; line-height: 1;
  }
  .product-kicker { top: 268px; font-size: 64px; font-weight: 400; }
  .product-name { top: 364px; font-size: 92px; font-weight: 400; }
  .product-desc {
    position: absolute; left: 0; width: 100%; top: 500px; text-align: center;
    font-family: "Arimo", sans-serif; font-weight: 700; font-size: 24px;
    color: var(--ink-dark); z-index: 2;
  }
  .facts {
    position: absolute; left: 26px; top: 1022px;
    font-family: "Arimo", sans-serif; font-size: 20px; line-height: 27px;
    color: var(--text-light);
  }
  .importer-lead {
    position: absolute; left: 259px; top: 1050px;
    font-family: "Arimo", sans-serif; font-size: 20px; color: var(--text-light);
  }
  .importer-badge {
    position: absolute; left: 392px; top: 987px; width: 212px; height: 84px;
    background: var(--badge-bg);
    display: flex; align-items: center; gap: 10px; padding: 0 12px;
  }
  .importer-badge .dot {
    flex: none; width: 14px; height: 14px; border-radius: 50%;
    background: var(--badge-ink);
  }
  .importer-badge .name {
    font-family: "Arimo", sans-serif; font-size: 17px; line-height: 21px;
    color: var(--badge-ink); text-transform: uppercase;
  }
</style>
</head>
<body>
<div class="canvas">
  <section class="label">
    <div class="moon"></div>
    <h2 class="product-kicker">Organic</h2>
    <h1 class="product-name">Hoshiba Matcha</h1>

    <svg class="hills" viewBox="0 0 644 1091" aria-hidden="true">
      <path d="M0,548 C120,560 250,605 400,636 C500,656 580,676 644,690 L644,705 C580,690 500,670 400,650 C250,620 120,575 0,560 Z"
            fill="var(--leaf-deep)" opacity="0.55"/>
      <path d="M0,560 C120,575 250,620 400,650 C500,670 580,690 644,705 L644,1091 L0,1091 Z"
            fill="var(--leaf-dark)"/>
    </svg>

    <p class="product-desc">Powdered Organic Green Tea</p>

    <div class="facts">
      <p>Product of Japan</p>
      <p>Green Tea 100%</p>
    </div>
    <p class="importer-lead">Imported by</p>
    <div class="importer-badge">
      <span class="dot"></span>
      <span class="name">Calm Harbor Leaf Merchants</span>
    </div>
  </section>
</div>
</body>
</html>
```